Custom Home Builder Needs a Website

Harbor Stone Builders Ltd. requires a clean professional 5 page website - Home, About Us, Gallery (Interior and Exterior), Our Process and Contact Us(with registration form). We are a home builder who also has homes for sale. Also please have a place for video embedding. Editable fields by user. Using the stationery 'feel' that is attached. Need social media links. If you require any additional files, please request.

Target Market(s)

Families and professionals

Industry/Entity Type

Home Builder

Coding

Coded - Design and coding required

Number of Pages Required

5+ page

Font styles to use
Sans Serif
Other font styles liked:
• Lato

Requirements
Must have
• Editable by user
• Register Button
• Place to put home models for sale - preferably on the first page
• 5 page website -
• -Home
• -About Us
• -Gallery (Interior and Exterior)
• -Our Process
• -Contact Us.
Nice to have
• Themed similar to current stationery
• place for video embedding
• Try some darker backgrounds
• Change pictures to B/W if works for design
Should not have
• cartoonish type of content

```html
<!DOCTYPE html>
<html lang="en">
<head>
<meta charset="utf-8">
<title>Harbor Stone Builders Ltd.</title>
<link href="https://fonts.googleapis.com/css2?family=Exo+2:wght@400;500;600&family=Montserrat:wght@400;600;700&family=Open+Sans:wght@400;600&display=swap" rel="stylesheet">
<style>
:root{
  --green:#2a8a1f;
  --green-dark:#1c6a14;
  --green-deep:#144f0e;
  --ink:#1d1d1d;
  --text:#555;
  --grey-bg:#e9e9e9;
  --footer:#232323;
  --line:#cfcfcf;
}
*{margin:0;padding:0;box-sizing:border-box}
html,body{width:1200px;height:2903px;overflow:hidden;background:#fff}
body{position:relative;font-family:"Open Sans",sans-serif;color:var(--text)}
.abs{position:absolute}

/* header */
.top-rule{left:0;top:0;width:1200px;height:4px;background:var(--green)}
.hours-tab{left:720px;top:0;width:364px;height:35px;display:flex;border-radius:0 0 14px 14px;overflow:hidden;font:600 14px "Montserrat",sans-serif;color:#fff}
.hours-tab .hours{flex:0 0 190px;background:var(--green);display:flex;align-items:center;justify-content:center;gap:8px}
.hours-tab .phone{flex:1;background:#9a9a9a;display:flex;align-items:center;justify-content:center;gap:8px;font-size:17px}
.brand{left:68px;top:40px;display:flex;align-items:center;gap:12px}
.brand-mark{width:40px;height:40px;background:var(--green)}
.brand-name{font:700 21px "Montserrat",sans-serif;color:var(--green-dark);line-height:1.15;width:210px}
.main-nav{left:561px;top:81px;display:flex;gap:0;font:700 13px "Montserrat",sans-serif;color:var(--ink)}
.main-nav a{display:block;height:37px;line-height:37px;padding:0 22px;text-decoration:none;color:inherit}
.main-nav a.active{background:var(--green);color:#fff;border-radius:3px}

/* hero */
.hero{left:0;top:143px;width:1200px;height:554px;background:linear-gradient(180deg,#d7dadd 0%,#8b8f93 35%,#5c5e5a 65%,#4e6e2f 100%)}
.reg-form{left:815px;top:240px;width:325px;height:335px;background:var(--green);padding:30px 24px}
.reg-form h2{font:500 23px "Exo 2",sans-serif;color:#fff;letter-spacing:1px;margin-bottom:22px}
.field{height:29px;background:#f2f2f2;margin-bottom:11px;display:flex;align-items:center;font-size:12px;color:#555}
.field .ic{width:30px;height:100%;display:flex;align-items:center;justify-content:center;border-right:1px solid #ddd;margin-right:10px}
.field.msg{height:64px;align-items:flex-start;padding-top:7px}
.field.msg .ic{height:16px;border:0}
.submit{margin-top:6px;width:114px;height:36px;background:linear-gradient(#b5b5b5,#8b8b8b);color:#fff;font:600 13px "Montserrat",sans-serif;display:flex;align-items:center;justify-content:center;letter-spacing:1px}

/* what we do */
.section-title{width:1200px;left:0;text-align:center;font:600 31px "Exo 2",sans-serif;color:var(--ink);letter-spacing:1.5px}
.intro{left:75px;top:820px;width:1050px;text-align:center;font-size:15.5px;line-height:1.72;color:#666}
.service h3{font:700 17px "Montserrat",sans-serif;color:var(--ink);margin-bottom:6px}
.service p{font-size:14.5px;line-height:1.6;color:#666}
.service.left{text-align:right}
.arc-name{left:455px;top:1110px;width:290px;text-align:center;font:700 30px "Montserrat",sans-serif;color:var(--green)}

/* mission */
.mission{left:0;top:1250px;width:1200px;height:465px}
.mission-bg{position:absolute;inset:0;background:linear-gradient(180deg,#2f8e24 0%,#247a1a 50%,#1f6d16 100%)}
.mission h2{position:absolute;left:340px;top:92px;width:520px;text-align:center;font:500 31px "Exo 2",sans-serif;color:#fff;letter-spacing:1.5px;border-top:1px solid rgba(255,255,255,.5);border-bottom:1px solid rgba(255,255,255,.5);padding:10px 0}
.mission .copy{position:absolute;left:100px;top:182px;width:1000px;text-align:center;color:#fff;font-size:14.8px;line-height:1.75}
.mission .copy p+p{margin-top:24px}

/* video */
.video{left:302px;top:1902px;width:547px;height:279px;background:linear-gradient(135deg,#2a2a2a,#111 60%,#1d1d1d);border:2px solid #3a3a3a}
.play{position:absolute;left:233px;top:80px;width:84px;height:84px;border-radius:50%;border:4px solid #bdbdbd;background:rgba(60,60,60,.85)}
.controls{position:absolute;left:0;bottom:0;width:100%;height:38px;background:#1a1a1a;display:flex;align-items:center;padding:0 16px;gap:16px}
.track{flex:1;height:4px;background:#ddd;position:relative}
.track span{position:absolute;left:0;top:0;height:100%;width:40%;background:var(--green)}

/* testimonials */
.testimonials{left:0;top:2254px;width:1200px;height:364px;background:var(--grey-bg)}
.t-title{left:0;top:2318px;width:1200px;text-align:center;font:400 31px "Exo 2",sans-serif;color:var(--ink);letter-spacing:2px}
.avatar{width:96px;height:96px;border-radius:50%;border:4px solid #fff;background:linear-gradient(#9a9a9a,#6e6e6e);box-shadow:0 2px 6px rgba(0,0,0,.2)}
.t-card{width:327px;height:120px;background:#fff;box-shadow:0 2px 6px rgba(0,0,0,.15);padding:14px 20px;font-size:10.5px;line-height:1.55;color:#777}
.t-card .who{margin-top:14px;font-size:10.5px;color:#333}
.t-arrow{font:400 34px "Montserrat",sans-serif;color:#bbb}
.dots{left:575px;top:2567px;display:flex;gap:12px}
.dots i{width:8px;height:8px;border-radius:50%;background:#bbb}
.dots i:first-child{background:#333}

/* footer */
.site-footer{left:0;top:2618px;width:1200px;height:285px;background:var(--footer)}
.f-brand{left:0;top:2676px;width:1200px;text-align:center;font:700 26px "Montserrat",sans-serif;color:#c9c9c9}
.copyright{left:0;top:2762px;width:1200px;text-align:center;font-size:14px;color:#9a9a9a}
.social{left:505px;top:2811px;display:flex;gap:20px}
.social a{width:30px;height:30px;border-radius:50%;background:#3a3a3a;display:block}
</style>
</head>
<body>

<header>
  <div class="abs top-rule"></div>
  <div class="abs hours-tab">
    <div class="hours">
      <svg width="16" height="16" viewBox="0 0 16 16"><circle cx="8" cy="8" r="6.5" fill="none" stroke="#fff" stroke-width="1.6"/><path d="M8 4v4l3 2" stroke="#fff" stroke-width="1.6" fill="none"/></svg>
      Mon-Fri: 9AM-5PM
    </div>
    <div class="phone">
      <svg width="18" height="18" viewBox="0 0 18 18"><circle cx="9" cy="9" r="8" fill="none" stroke="#fff" stroke-width="1.4"/><path d="M6 5l2 2-1 1c.5 1.3 1.7 2.5 3 3l1-1 2 2-1.5 1.5C8.5 13 5 9.5 4.5 6.5z" fill="#fff"/></svg>
      306.555.0142
    </div>
  </div>
  <div class="abs brand">
    <div class="brand-mark"></div>
    <div class="brand-name">Harbor Stone Builders Ltd.</div>
  </div>
  <nav class="abs main-nav">
    <a class="active" href="#">HOME</a>
    <a href="#">ABOUT US</a>
    <a href="#">GALLERY</a>
    <a href="#">OUR PROCESS</a>
    <a href="#">CONTACT US</a>
  </nav>
</header>

<section>
  <div class="abs hero" role="img" aria-label="Photograph of a two-storey craftsman family home with stone base, garage and green lawn under an overcast sky"></div>
  <form class="abs reg-form">
    <h2>REGISTRATION FORM</h2>
    <div class="field"><span class="ic"><svg width="12" height="12" viewBox="0 0 12 12"><circle cx="6" cy="3.5" r="2.5" fill="#666"/><path d="M1 12c0-3 2.2-5 5-5s5 2 5 5z" fill="#666"/></svg></span>Name</div>
    <div class="field"><span class="ic"><svg width="12" height="12" viewBox="0 0 12 12"><path d="M2 1l2.5 2.5-1.2 1.2c.6 1.5 1.8 2.7 3.3 3.3l1.2-1.2L10.3 9.3 8.8 10.8C5 10 2 7 1.2 3.2z" fill="#666"/></svg></span>Phone</div>
    <div class="field"><span class="ic"><svg width="13" height="10" viewBox="0 0 13 10"><rect x=".5" y=".5" width="12" height="9" fill="#666"/><path d="M1 1l5.5 4.5L12 1" stroke="#eee" fill="none"/></svg></span>Email</div>
    <div class="field msg"><span class="ic"><svg width="13" height="10" viewBox="0 0 13 10"><rect x=".5" y=".5" width="12" height="9" fill="#666"/><path d="M1 1l5.5 4.5L12 1" stroke="#eee" fill="none"/></svg></span>Message</div>
    <div class="submit">SUBMIT</div>
  </form>
</section>

<section>
  <h2 class="abs section-title" style="top:755px">WHAT WE DO</h2>
  <p class="abs intro">Dale Marren has many years of experience in the home building industry. He has completed many significant projects throughout western Canada over the past 25 years. His experience ranges from large scale town house projects, including high-rise tower construction, to commercial Developments where you can do your day to day shopping.</p>

  <svg class="abs" style="left:330px;top:970px" width="540" height="265" viewBox="0 0 540 265">
    <path d="M15 256 A255 255 0 0 1 525 256" fill="none" stroke="var(--green)" stroke-width="3"/>
    <circle cx="15" cy="256" r="4" fill="var(--green-deep)"/>
    <circle cx="525" cy="256" r="4" fill="var(--green-deep)"/>
    <circle cx="27" cy="170" r="7" fill="#9a9a9a"/>
    <circle cx="513" cy="170" r="7" fill="#9a9a9a"/>
    <circle cx="135" cy="42" r="7" fill="#9a9a9a"/>
    <circle cx="405" cy="42" r="7" fill="#9a9a9a"/>
  </svg>
  <div class="abs arc-name">Harbor Stone Builders</div>

  <div class="abs service left" style="left:80px;top:980px;width:310px">
    <h3>NEW HOME CONSTRUCTION</h3>
    <p>Solution for families that need<br>an extra level of care</p>
  </div>
  <div class="abs service left" style="left:40px;top:1112px;width:266px">
    <h3>LAND DEVELOPMENT</h3>
    <p>From companionship services<br>to hospice care support</p>
  </div>
  <div class="abs service" style="left:790px;top:984px;width:320px">
    <h3>RENOVATIONS</h3>
    <p>We provide transportation services<br>you can rely on</p>
  </div>
  <div class="abs service" style="left:868px;top:1112px;width:300px">
    <h3>CONSULTING/PARTNERSHIPS</h3>
    <p>We are looking for caring individuals<br>to join our teams</p>
  </div>
</section>

<section class="abs mission">
  <div class="mission-bg" role="img" aria-label="Interior photograph of a modern living room under a green tint"></div>
  <svg style="position:absolute;left:0;top:0" width="1200" height="40" viewBox="0 0 1200 40"><path d="M0 0H1200V8Q600 40 0 8Z" fill="#fff"/></svg>
  <h2>MISSION STATEMENT</h2>
  <div class="copy">
    <p>Our projects start with a vision, with a priority to build attractive, appealing and functional homes. To build the home that suits you best, we will spend time getting to know you and your family, with your specific wants and needs. Our goal is to put the same thought and care in every project that we would put into our own home.</p>
    <p>With our professional construction services, we strive for excellence in quality, functionality, sustainability and livability in every construction project we do. This translates into an inviting home with a layout that flows, lines that are pleasing to the eye, and attention to detail that will satisfy even those with the most discerning taste. We will help you learn to maintain your home, giving you the home that will last for generations and stand the test of time.</p>
  </div>
</section>

<section>
  <h2 class="abs section-title" style="top:1797px">WATCH VIDEOS</h2>
  <div class="abs video">
    <div class="play"><svg width="76" height="76" viewBox="0 0 76 76"><path d="M30 22l24 16-24 16z" fill="#e5e5e5"/></svg></div>
    <div class="controls">
      <svg width="14" height="14" viewBox="0 0 14 14"><path d="M2 1l11 6-11 6z" fill="#fff"/></svg>
      <div class="track"><span></span></div>
      <svg width="18" height="14" viewBox="0 0 18 14"><path d="M1 4h4l5-4v14l-5-4H1z" fill="#fff"/><path d="M13 3q3 4 0 8" stroke="#fff" fill="none" stroke-width="1.5"/></svg>
      <svg width="16" height="14" viewBox="0 0 16 14"><path d="M1 5V1h4M11 1h4v4M15 9v4h-4M5 13H1V9" stroke="#fff" fill="none" stroke-width="2"/></svg>
    </div>
  </div>
</section>

<section>
  <div class="abs testimonials"></div>
  <h2 class="abs t-title">CLIENT TESTIMONIALS</h2>
  <div class="abs t-arrow" style="left:82px;top:2448px">‹</div>
  <div class="abs t-arrow" style="left:1100px;top:2448px">›</div>
  <div class="abs avatar" style="left:150px;top:2428px" role="img" aria-label="Portrait photo of client Evan Kessler"></div>
  <div class="abs t-card" style="left:265px;top:2417px">
    <p>Our new home was finished on schedule and every detail felt considered. The crew listened closely, kept us informed at every step and delivered a layout that suits our family.</p>
    <p class="who">Evan Kessler – CEO of Norvale Group –</p>
  </div>
  <div class="abs t-card" style="left:611px;top:2417px;text-align:center">
    <p>From the first meeting to handing over the keys, the team was honest and careful. Quality work, fair pricing and a home we are proud of.</p>
    <p class="who">– Mara Olsen – CEO of Norvale Group –</p>
  </div>
  <div class="abs avatar" style="left:958px;top:2428px" role="img" aria-label="Portrait photo of client Mara Olsen"></div>
  <div class="abs dots"><i></i><i></i><i></i></div>
</section>

<footer>
  <div class="abs site-footer"></div>
  <div class="abs f-brand">Harbor Stone Builders Ltd.</div>
  <p class="abs copyright">Copyright © 2016. Harbor Stone Builders. All rights reserved</p>
  <div class="abs social">
    <a href="#" aria-label="Social link 1"></a>
    <a href="#" aria-label="Social link 2"></a>
    <a href="#" aria-label="Social link 3"></a>
    <a href="#" aria-label="Social link 4"></a>
  </div>
</footer>

</body>
</html>
```